Business Card Design Project

Industry/Entity Type

Business

Contact Information for Business Card

The Mercy Hill Gospel Choir
Dean Farrow, Minister of Music

The Harvest Covenant Church of Greenfield
Founded 1792

Blinkr @themhgc
Picturo mercyhillgc
Friendwall friendwall.example/mhgc408
Website: mercyhillgc.example
For Bookings: (555) 552-MHGC
4827 Marlowe Avenue, Philadelphia, PA 19144

Back of the Card
Music and Cd's Recordings Available On
Choirs Website and Also
Tunevault, Orbita Music, Disc Pony (the music online logo)

```html
<!DOCTYPE html>
<html lang="en">
<head>
<meta charset="utf-8">
<title>Mercy Hill Gospel Choir – Business Card</title>
<link rel="stylesheet" href="https://fonts.googleapis.com/css2?family=Lato:wght@400;700&family=Pinyon+Script&display=swap">
<style>
  :root {
    --page-bg: #3a3230;
    --card-white: #ffffff;
    --ink: #222222;
    --ink-soft: #444444;
    --choir-red: #c4202c;
    --panel-blue: #2f6db3;
    --panel-grey: #dcdcda;
    --mark-grey: #9a9a96;
  }
  * { box-sizing: border-box; margin: 0; padding: 0; }
  html, body { width: 1200px; height: 810px; overflow: hidden; }
  body {
    background: var(--page-bg);
    font-family: "Lato", Arial, sans-serif;
    color: var(--ink);
    position: relative;
  }
  .card {
    position: absolute;
    width: 560px;
    height: 320px;
    background: var(--card-white);
    box-shadow: 0 10px 24px rgba(0,0,0,.45);
    overflow: hidden;
  }
  .card--back { left: 40px; top: 70px; }
  .card--front { left: 600px; top: 420px; }

  .choir-mark {
    position: absolute;
    display: flex;
    align-items: center;
    gap: 10px;
    font-family: "Lato", Arial, sans-serif;
    font-weight: 700;
    font-size: 20px;
    color: var(--choir-red);
    white-space: nowrap;
  }
  .choir-mark .square { width: 16px; height: 16px; background: var(--mark-grey); flex: none; }

  /* back side */
  .card--back .choir-mark { left: 0; width: 100%; justify-content: center; top: 82px; }
  .back-tagline { position: absolute; top: 130px; width: 100%; text-align: center; font-size: 14px; color: var(--ink-soft); }
  .back-url { position: absolute; top: 154px; width: 100%; text-align: center; font-size: 13px; color: var(--ink-soft); }
  .stores { position: absolute; top: 224px; left: 0; width: 100%; display: flex; justify-content: space-around; align-items: center; }
  .store { font-size: 22px; font-weight: 700; color: var(--ink); }

  /* front side */
  .front-shapes { position: absolute; inset: 0; }
  .card--front .choir-mark { left: 28px; top: 82px; }
  .church { position: absolute; right: 18px; top: 24px; width: 290px; text-align: center;
    font-family: "Pinyon Script", cursive; font-size: 17px; line-height: 1.25; color: var(--ink); }
  .socials { position: absolute; left: 22px; top: 180px; list-style: none; color: #fff; font-size: 14px; line-height: 24px; }
  .socials li { display: flex; align-items: center; gap: 9px; }
  .socials .mark { width: 10px; height: 10px; background: #fff; display: inline-block; }
  .socials .mark--round { border-radius: 50%; }
  .identity { position: absolute; right: 22px; top: 114px; text-align: right; }
  .identity .name { font-size: 19px; color: var(--ink); }
  .identity .role { font-size: 13px; color: var(--ink-soft); margin-top: 2px; }
  .contact { position: absolute; right: 22px; top: 196px; text-align: right; font-size: 15px; line-height: 20px; color: var(--ink); }
  .contact .row { display: flex; justify-content: flex-end; align-items: flex-start; gap: 8px; }
  .contact .row--phone { margin-top: 8px; }
  .contact svg { flex: none; margin-top: 3px; }
</style>
</head>
<body>

  <section class="card card--back" aria-label="Card back">
    <div class="choir-mark"><span class="square"></span>The Mercy Hill Gospel Choir</div>
    <p class="back-tagline">Music and Cd's Recordings Available On</p>
    <p class="back-url">www.mercyhillgc.example</p>
    <div class="stores">
      <span class="store">Tunevault</span>
      <span class="store">Orbita Music</span>
      <span class="store">Disc Pony</span>
    </div>
  </section>

  <section class="card card--front" aria-label="Card front">
    <svg class="front-shapes" width="560" height="320" viewBox="0 0 560 320" aria-hidden="true">
      <polygon points="0,165 318,165 343,320 0,320" fill="var(--panel-blue)"/>
      <polygon points="331,165 560,165 560,320 356,320" fill="var(--panel-grey)"/>
    </svg>
    <div class="choir-mark"><span class="square"></span>The Mercy Hill Gospel Choir</div>
    <p class="church">The Harvest Covenant Church of Greenfield<br>Founded 1792</p>

    <ul class="socials">
      <li><span class="mark"></span>friendwall.example/mhgc408</li>
      <li><span class="mark"></span>mercyhillgc</li>
      <li><span class="mark"></span>@themhgc</li>
      <li><span class="mark mark--round"></span>mercyhillgc.example</li>
    </ul>

    <div class="identity">
      <p class="name">The Mercy Hill Gospel Choir</p>
      <p class="role">Dean Farrow, Minister of Music</p>
    </div>

    <div class="contact">
      <div class="row">
        <span>4827 Marlowe Avenue,<br>Philadelphia,<br>PA 19144</span>
        <svg width="12" height="16" viewBox="0 0 12 16"><path d="M6 0a6 6 0 0 0-6 6c0 4.5 6 10 6 10s6-5.5 6-10a6 6 0 0 0-6-6zm0 8.5A2.5 2.5 0 1 1 6 3.5a2.5 2.5 0 0 1 0 5z" fill="var(--ink)"/></svg>
      </div>
      <div class="row row--phone">
        <span>(555) 552-MHGC</span>
        <svg width="12" height="16" viewBox="0 0 12 16"><path d="M3 0h3l1 4-2 1.5c.6 2 1.6 3.5 3 5L10 9l2 3-1 3c-5-1-10-7-10-13z" fill="var(--ink)"/></svg>
      </div>
    </div>
  </section>

</body>
</html>
```